Dental office post card

Dental office promotion to new community
POST CARD SIZE 6" x 11" EDDM
Phone numner 832 617 2098.

Target Market(s)

mainly adults and families

Font styles to use
Sans Serif

Colors

Designer to choose colors to be used in the design.

Requirements
Must have
• Office pictures please see attched
• Doctor's picture please see attached
• Modern simple design
• Not too many words
• OPEN EVENINGS, SATURDAYS AND SUNDAYS
• Emergency and walk-in welcome
• FINANCING AVAILABLE
• MOST PPO INSURANCES ACCEPTED
• CONVENIENT LOCATION AT THE CORNER OF FENNEL RD AND HIGHWAY 47
• Phone number (832) 617 -2098 please do not put the number on the website.
Nice to have
• brightsmilekerrow.example
• Dr. Hale Varno
• Friendly local dentist to serve your dental needs
• Westmere School of dentistry
• Ridgefield College, BA, Molecular Cell Biology
• Coastal Guard Corps veteran, captain, dental officer

```html
<!DOCTYPE html>
<html lang="en">
<head>
<meta charset="utf-8">
<title>Brightside Dental – EDDM Postcard</title>
<link href="https://fonts.googleapis.com/css2?family=Montserrat:wght@400;500;600;700;800&family=Open+Sans:wght@400;600&display=swap" rel="stylesheet">
<style>
  :root{
    --teal:#1a8ea3;
    --teal-dark:#0f6b7c;
    --navy:#1d3a4a;
    --red:#d9322b;
    --ink:#2b2f33;
    --muted:#6b7379;
    --paper:#ffffff;
    --stage:#ececec;
    --photo-cool:#c9d3d8;
    --photo-warm:#b9a48e;
  }
  *{box-sizing:border-box;margin:0;padding:0}
  html,body{width:690px;height:1200px;overflow:hidden;background:var(--stage)}
  body{position:relative;font-family:"Open Sans",Arial,sans-serif;color:var(--ink)}
  .card{position:absolute;left:20px;width:650px;height:355px;background:var(--paper);overflow:hidden;box-shadow:0 2px 8px rgba(0,0,0,.15)}
  .card-front{top:225px}
  .card-back{top:620px}
  .brand-name{font-family:"Montserrat",sans-serif;font-weight:600;font-size:21px;color:var(--teal-dark);line-height:1;white-space:nowrap}
  .photo{position:absolute}
  /* front */
  .front-brand{position:absolute;left:20px;top:30px}
  .office-photo{left:300px;top:0;width:170px;height:80px;background:linear-gradient(135deg,#e6ebee,var(--photo-cool) 60%,#8fa2ab)}
  .tooth-photo{left:470px;top:0;width:180px;height:280px;background:radial-gradient(circle at 45% 55%,#ffffff 0,#eef1f3 35%,#cfd6da 100%)}
  .hero-band{position:absolute;left:0;top:80px;width:470px;height:175px;background:var(--teal)}
  .doctor-photo{left:20px;top:86px;width:130px;height:169px;background:linear-gradient(180deg,#6fb4c2,#3c7e8d)}
  .hero-copy{position:absolute;left:165px;top:96px;width:300px;color:#fff}
  .hero-title{font-family:"Montserrat",sans-serif;font-weight:700;font-size:17px;margin-bottom:12px;white-space:nowrap}
  .perks{list-style:none}
  .perks li{display:flex;align-items:center;gap:7px;font-size:10.5px;margin-bottom:6px}
  .perks svg{flex:none}
  .location-bar{position:absolute;left:0;top:255px;width:470px;height:25px;background:var(--teal-dark);color:#fff;font-family:"Montserrat",sans-serif;font-size:11px;font-weight:500;display:flex;align-items:center;justify-content:flex-end;padding-right:14px}
  .location-bar b{font-weight:700;margin:0 3px}
  .doctor-id{position:absolute;left:20px;top:287px}
  .doctor-name{font-family:"Montserrat",sans-serif;font-weight:700;font-size:16px;color:var(--teal-dark)}
  .doctor-creds{font-size:6.5px;color:var(--muted);line-height:1.4;margin-top:2px}
  .contact{position:absolute;left:300px;top:286px;width:330px;text-align:center}
  .emergency{display:inline-block;background:var(--red);color:#fff;font-family:"Montserrat",sans-serif;font-weight:700;font-size:11px;padding:4px 18px;letter-spacing:.5px}
  .appt{font-family:"Montserrat",sans-serif;font-size:11px;color:var(--teal-dark);font-weight:600;margin:4px 0 3px}
  .contact-line{display:flex;justify-content:center;align-items:center;gap:6px;font-size:9px;color:var(--ink)}
  .contact-line .phone{font-weight:700;color:var(--navy)}
  /* back */
  .back-brand{position:absolute;left:20px;top:22px}
  .xray-photo{left:10px;top:55px;width:70px;height:140px;background:linear-gradient(180deg,#f1f3f4,#c7cdd1)}
  .hall-photo{left:85px;top:55px;width:120px;height:140px;background:linear-gradient(180deg,#d8cdbd,var(--photo-warm) 60%,#8a7866)}
  .lounge-photo{left:210px;top:55px;width:110px;height:140px;background:linear-gradient(160deg,#e3ddd3,#b78e6c 70%,#7f6957)}
  .welcome-band{position:absolute;left:0;top:205px;width:325px;height:150px;background:var(--teal);color:#fff;padding:14px 14px}
  .welcome-title{font-family:"Montserrat",sans-serif;font-weight:700;font-size:12px;margin-bottom:6px}
  .welcome-text{width:185px;font-size:7px;line-height:1.5}
  .call-box{position:absolute;right:14px;top:30px;text-align:center;font-family:"Montserrat",sans-serif}
  .call-box small{display:block;font-size:9px}
  .call-box strong{display:block;font-size:11px;margin-bottom:3px}
  .call-box .phone{font-size:12px;font-weight:700}
  .indicia{position:absolute;right:18px;top:18px;width:74px;height:54px;border:1px solid var(--ink);font-size:6.5px;text-align:center;line-height:1.35;padding-top:5px;font-family:"Montserrat",sans-serif}
  .address-box{position:absolute;left:400px;top:232px;width:110px;height:40px;border:1px solid var(--muted);font-size:6.5px;padding:6px 8px;line-height:1.4}
</style>
</head>
<body>

<section class="card card-front" aria-label="Postcard front">
  <div class="brand-name front-brand">Brightside Dental</div>
  <div class="photo office-photo" role="img" aria-label="Photo of the dental treatment room"></div>
  <div class="photo tooth-photo" role="img" aria-label="Image of a white tooth with a dental mirror"></div>

  <div class="hero-band"></div>
  <div class="photo doctor-photo" role="img" aria-label="Portrait of the dentist in scrubs"></div>
  <div class="hero-copy">
    <h1 class="hero-title">Open Evenings and Saturdays</h1>
    <ul class="perks">
      <li><svg width="11" height="11" viewBox="0 0 12 12"><path d="M2 6.5l2.5 2.5L10 3" fill="none" stroke="#fff" stroke-width="2"/></svg>Walk in and emergency welcome</li>
      <li><svg width="11" height="11" viewBox="0 0 12 12"><path d="M2 6.5l2.5 2.5L10 3" fill="none" stroke="#fff" stroke-width="2"/></svg>We value your time: Minimum wait time</li>
      <li><svg width="11" height="11" viewBox="0 0 12 12"><path d="M2 6.5l2.5 2.5L10 3" fill="none" stroke="#fff" stroke-width="2"/></svg>Full service modern dentistry</li>
      <li><svg width="11" height="11" viewBox="0 0 12 12"><path d="M2 6.5l2.5 2.5L10 3" fill="none" stroke="#fff" stroke-width="2"/></svg>Call for dental implant special promotion</li>
      <li><svg width="11" height="11" viewBox="0 0 12 12"><path d="M2 6.5l2.5 2.5L10 3" fill="none" stroke="#fff" stroke-width="2"/></svg>Financing available</li>
    </ul>
  </div>
  <div class="location-bar">Convenient location on <b>Fennel Rd</b> and <b>Highway 47</b></div>

  <div class="doctor-id">
    <div class="doctor-name">Dr. Hale Varno</div>
    <div class="doctor-creds">Westmere School of dentistry<br>Ridgefield College, BA, Molecular Cell Biology<br>Coastal Guard Corps veteran, captain, dental officer</div>
  </div>
  <div class="contact">
    <div class="emergency">EMERGENCY DENTAL CARE</div>
    <div class="appt">Make an Appointment</div>
    <div class="contact-line">
      <svg width="10" height="10" viewBox="0 0 24 24"><path d="M6.6 10.8a15 15 0 006.6 6.6l2.2-2.2a1 1 0 011-.25 11.4 11.4 0 003.6.57 1 1 0 011 1V20a1 1 0 01-1 1A17 17 0 013 4a1 1 0 011-1h3.5a1 1 0 011 1 11.4 11.4 0 00.57 3.6 1 1 0 01-.25 1z" fill="#1a8ea3"/></svg>
      <span class="phone">832 617 2098</span>
      <span>•</span>
      <span>brightsmilekerrow.example</span>
    </div>
  </div>
</section>

<section class="card card-back" aria-label="Postcard back">
  <div class="brand-name back-brand">Brightside Dental</div>
  <div class="photo xray-photo" role="img" aria-label="Photo of the panoramic x-ray machine"></div>
  <div class="photo hall-photo" role="img" aria-label="Photo of the office hallway"></div>
  <div class="photo lounge-photo" role="img" aria-label="Photo of the waiting lounge"></div>

  <div class="welcome-band">
    <h2 class="welcome-title">Welcome to Brightside Dental</h2>
    <p class="welcome-text">We are proud to bring friendly, modern dental care to your neighborhood. Our team welcomes adults and families with gentle treatment, flexible hours and most PPO insurances accepted.</p>
    <div class="call-box">
      <small>Call for</small>
      <strong>Appointment</strong>
      <span class="phone">(832) 617 -2098</span>
    </div>
  </div>

  <div class="indicia">PRSRT STD<br>ECRWSS<br>U.S. POSTAGE<br>PAID<br>EDDM RETAIL</div>
  <div class="address-box">Local<br>Postal Customer</div>
</section>

</body>
</html>
```